Professional Business Card - TWO SIDES

I need a new business card design to be used by myself and my employees. I would like a professional card and for the front I thought I would like a dark blue thatch with our logo in a raised gold foil on top of it. On the other side I would like name, position, and contact info. I've uploaded our old design for an example of the info used.

Target Market(s)

Business Clients

Industry/Entity Type

CPA Firm

Contact Information for Business Card

Logo, Name, Title, Address, Phone Numbers, Website address, Email Address

Font styles to use
Serif
Sans Serif

Colors
0054AA
0677BA
7BADD7
CADEEF
E8F1F8
0094D4
00A9DD
6FCCEA
C7EBF8
E9F6FB

Requirements
Must have
• Modern Professional Look
Nice to have
• Logo in Gold Foil or ability to have is raised. I like our logo in a single color
Should not have
• I've uploaded old business card

```html
<!DOCTYPE html>
<html lang="en">
<head>
<meta charset="utf-8">
<title>Hale &amp; Hale Business Card</title>
<link href="https://fonts.googleapis.com/css2?family=Roboto:wght@400;700;900&display=swap" rel="stylesheet">
<style>
  :root {
    --backdrop: #ebebeb;
    --navy: #27405f;
    --gold: #c9a23c;
    --paper: #f7f7f7;
    --ink: #2b2b2b;
    --muted: #555555;
    --card-shadow: 0 6px 18px rgba(0,0,0,0.12);
  }
  * { box-sizing: border-box; margin: 0; padding: 0; }
  html, body {
    width: 1199px; height: 1200px; overflow: hidden;
    background: var(--backdrop);
    font-family: "Roboto", Arial, sans-serif;
  }
  .sheet {
    position: relative; width: 1199px; height: 1200px;
  }
  .card {
    position: absolute; left: 160px;
    width: 880px; height: 503px;
    box-shadow: var(--card-shadow);
    overflow: hidden;
  }
  .card-front {
    top: 60px;
    background: var(--navy);
    display: flex; align-items: center; justify-content: center;
  }
  .wordmark {
    color: var(--gold);
    font-weight: 900;
    text-transform: uppercase;
    letter-spacing: 2px;
    white-space: nowrap;
  }
  .card-front .wordmark { font-size: 86px; }
  .card-back {
    top: 637px;
    background: var(--paper);
    display: flex;
  }
  .brand-band {
    width: 240px; height: 100%;
    background: var(--navy);
    position: relative;
  }
  .brand-band .wordmark {
    position: absolute; left: 50%; top: 50%;
    font-size: 58px;
    transform: translate(-50%, -50%) rotate(-90deg);
  }
  .details {
    flex: 1;
    padding: 70px 0 0 60px;
  }
  .person-name {
    color: var(--navy);
    font-size: 44px; font-weight: 700;
    line-height: 1.1;
  }
  .person-title {
    color: var(--muted);
    font-size: 22px; font-weight: 400;
    margin-top: 6px;
    letter-spacing: 0.5px;
  }
  .divider {
    width: 270px; height: 2px;
    background: var(--navy);
    margin: 18px 0 28px;
  }
  .contact-list { list-style: none; }
  .contact-item {
    display: flex; align-items: flex-start;
    margin-bottom: 20px;
  }
  .contact-icon {
    flex: none;
    width: 40px; height: 40px; border-radius: 50%;
    background: var(--navy);
    display: flex; align-items: center; justify-content: center;
    margin-right: 22px;
  }
  .contact-icon svg { width: 20px; height: 20px; }
  .contact-text {
    color: var(--ink);
    font-size: 23px; line-height: 1.25;
    padding-top: 7px;
  }
</style>
</head>
<body>
<main class="sheet">
  <section class="card card-front" aria-label="Card front">
    <span class="wordmark">Hale &amp; Hale</span>
  </section>

  <section class="card card-back" aria-label="Card back">
    <div class="brand-band">
      <span class="wordmark">Hale &amp; Hale</span>
    </div>
    <div class="details">
      <h1 class="person-name">Daniel Hale</h1>
      <p class="person-title">Managing Director</p>
      <div class="divider"></div>
      <ul class="contact-list">
        <li class="contact-item">
          <span class="contact-icon">
            <svg viewBox="0 0 24 24" aria-hidden="true"><path fill="#fff" d="M6.6 10.8a15.1 15.1 0 0 0 6.6 6.6l2.2-2.2a1 1 0 0 1 1-.25 11.4 11.4 0 0 0 3.6.57 1 1 0 0 1 1 1V20a1 1 0 0 1-1 1A17 17 0 0 1 3 4a1 1 0 0 1 1-1h3.5a1 1 0 0 1 1 1c0 1.25.2 2.45.57 3.57a1 1 0 0 1-.25 1z"/></svg>
          </span>
          <span class="contact-text">555.010.2200</span>
        </li>
        <li class="contact-item">
          <span class="contact-icon">
            <svg viewBox="0 0 24 24" aria-hidden="true"><rect x="3" y="5" width="18" height="14" rx="2" fill="#fff"/><path d="M4 7l8 6 8-6" fill="none" stroke="#27405f" stroke-width="1.8"/></svg>
          </span>
          <span class="contact-text">daniel@haleandhale.com<br>www.haleandhale.com</span>
        </li>
        <li class="contact-item">
          <span class="contact-icon">
            <svg viewBox="0 0 24 24" aria-hidden="true"><path fill="#fff" d="M12 2a7 7 0 0 0-7 7c0 5.2 7 13 7 13s7-7.8 7-13a7 7 0 0 0-7-7zm0 9.5A2.5 2.5 0 1 1 12 6.5a2.5 2.5 0 0 1 0 5z"/></svg>
          </span>
          <span class="contact-text">Blabla S Market Street Linden, MS 39000</span>
        </li>
      </ul>
    </div>
  </section>
</main>
</body>
</html>
```